Business Card Design - TORVEX
miles@torvex.example
Project: Business Card Design - TORVEX
Business Card Design - TORVEX - Telecommunications
Creative Brief
Professional
Miles Brandt
Vice President
www.torvex.example
Looking for a very well designed and eye catching business card that we can use into the future. Should be designed around the TORVEX logo and using the included radio images is just optional.
Digital Communications Coastline Fleet Relay Grid Cellphone Coverage Enhancement P25 - Public Safety Equipment Digital Radio Rentals Dispatch Consoles
milestor7 milestor7
Thanks for all the design ideas so far. I will be getting together with my team and will start providing feedback this afternoon. Best Wishes, Miles

```html
<!DOCTYPE html>
<html lang="en">
<head>
<meta charset="UTF-8">
<title>TORVEX Business Card</title>
<link href="https://fonts.googleapis.com/css2?family=Roboto+Condensed:ital,wght@0,400;0,700;1,700&family=Roboto:wght@400;500&display=swap" rel="stylesheet">
<style>
  :root {
    --page-bg: #e6e6e6;
    --card-dark: #121212;
    --card-light: #ffffff;
    --brand-red: #c8161d;
    --text-light: #ffffff;
    --text-grey: #7a7a7a;
    --text-dark: #3a3a3a;
    --divider: #c9c9c9;
  }
  * { margin: 0; padding: 0; box-sizing: border-box; }
  html, body { width: 1200px; height: 802px; overflow: hidden; }
  body {
    background: var(--page-bg);
    position: relative;
    font-family: "Roboto", Arial, sans-serif;
  }
  .card { position: absolute; box-shadow: 0 6px 18px rgba(0,0,0,.18); overflow: hidden; }

  /* Front: dark portrait card */
  .card-front {
    left: 157px; top: 138px; width: 300px; height: 525px;
    background: var(--card-dark);
  }
  .radio-photo {
    position: absolute; left: 0; top: 0; width: 300px; height: 345px;
    background:
      radial-gradient(ellipse 38% 48% at 52% 55%, #2e2e2e 0%, #232323 55%, rgba(18,18,18,0) 100%),
      linear-gradient(180deg, #1c1c1c 0%, #161616 60%, #121212 100%);
  }
  .brand-name {
    position: absolute; left: 0; right: 0; top: 66px;
    text-align: center;
    font-family: "Roboto Condensed", Arial, sans-serif;
    font-weight: 700; font-size: 22px; letter-spacing: 2px;
    color: var(--brand-red); line-height: 1;
  }
  .service-band {
    position: absolute; left: 0; top: 352px; width: 300px; height: 26px;
    background: var(--brand-red);
    display: flex; align-items: center; justify-content: flex-end;
    padding-right: 22px;
  }
  .service-band h2 {
    font-family: "Roboto Condensed", Arial, sans-serif;
    font-weight: 700; font-size: 15px; letter-spacing: .5px;
    color: var(--text-light); text-transform: uppercase;
  }
  .service-list {
    position: absolute; left: 18px; top: 392px; right: 12px;
    list-style: none;
    font-family: "Roboto Condensed", Arial, sans-serif;
    font-style: italic; font-weight: 700; font-size: 12.5px;
    line-height: 24px; color: var(--text-light); white-space: nowrap;
  }
  .service-list .sep { color: var(--brand-red); padding: 0 4px; }

  /* Back: white landscape card */
  .card-back {
    left: 518px; top: 251px; width: 525px; height: 300px;
    background: var(--card-light);
  }
  .identity {
    position: absolute; left: 42px; top: 128px;
  }
  .identity .name {
    font-family: "Roboto Condensed", Arial, sans-serif;
    font-weight: 700; font-size: 26px; color: var(--brand-red);
    text-transform: uppercase; letter-spacing: .3px; line-height: 1;
  }
  .identity .role {
    font-size: 12px; color: var(--text-grey); margin-top: 5px; text-align: right;
  }
  .divider {
    position: absolute; left: 228px; top: 100px; width: 1px; height: 100px;
    background: var(--divider);
  }
  .contact-list {
    position: absolute; left: 252px; top: 104px; list-style: none;
  }
  .contact-list li {
    display: flex; align-items: center; gap: 10px;
    font-size: 13px; color: var(--text-dark); height: 31px;
  }
  .contact-list svg { width: 14px; height: 14px; flex: none; }
</style>
</head>
<body>

  <section class="card card-front" aria-label="Card front">
    <div class="radio-photo" role="img" aria-label="Photograph of a black handheld digital two-way radio carrying the TORVEX name"></div>
    <p class="brand-name">TORVEX</p>
    <div class="service-band"><h2>Your Service</h2></div>
    <ul class="service-list">
      <li>Digital Communications<span class="sep">|</span>Coastline Fleet Relay Grid</li>
      <li>Cellphone Coverage Enhancement</li>
      <li>P25 - Public Safety Equipment</li>
      <li>Digital Radio Rentals<span class="sep">|</span>Dispatch Consoles</li>
    </ul>
  </section>

  <section class="card card-back" aria-label="Card back">
    <div class="identity">
      <p class="name">Miles Brandt</p>
      <p class="role">Vice President</p>
    </div>
    <div class="divider"></div>
    <ul class="contact-list">
      <li>
        <svg viewBox="0 0 24 24" aria-hidden="true"><path fill="#c8161d" d="M6.6 10.8a15.1 15.1 0 0 0 6.6 6.6l2.2-2.2c.3-.3.7-.4 1-.2 1.1.4 2.3.6 3.6.6.6 0 1 .4 1 1V20c0 .6-.4 1-1 1A17 17 0 0 1 3 4c0-.6.4-1 1-1h3.5c.6 0 1 .4 1 1 0 1.3.2 2.5.6 3.6.1.3 0 .7-.2 1z"/></svg>
        555-018-4721
      </li>
      <li>
        <svg viewBox="0 0 24 24" aria-hidden="true"><rect x="2" y="5" width="20" height="14" rx="2" fill="#c8161d"/><path d="M3 6.5l9 6 9-6" stroke="#fff" stroke-width="1.6" fill="none"/></svg>
        miles@torvex.example
      </li>
      <li>
        <svg viewBox="0 0 24 24" aria-hidden="true"><circle cx="12" cy="12" r="10" fill="#c8161d"/><path d="M2 12h20M12 2c3 3 3 17 0 20M12 2c-3 3-3 17 0 20" stroke="#fff" stroke-width="1.3" fill="none"/></svg>
        www.torvex.example
      </li>
    </ul>
  </section>

</body>
</html>
```